Need Help having my business card stand out

I am the owner of Pine Ridge Canine Coaching and would like for my business cards to stand out. I have been trying to keep designing them myself but I can't get what I have in my head on the card. I will try my best to post templates that I like for inspirations. I want something unique but elegant. I don't want in to look cartoony or cheesy. It needs to pop in a pet shop but also in a coffee shop or gym.

Target Market(s)

Dog owners, Married ,No young kids Jr High school kids and up (maybe kids on the way) Executives, Stay at home moms/wives, Small business owners

Industry/Entity Type

Dog Training

Contact Information for Business Card

Trevor Holloway, 555-304-7162, info@pineridgecanine.example, www.pineridgecanine.example

Colors

Designer to choose colors to be used in the design.

Requirements
Must have
• my logo
Should not have
• Cursive lettering

```html
<!DOCTYPE html>
<html lang="en">
<head>
<meta charset="utf-8">
<title>Pine Ridge Canine Coaching – Business Card</title>
<link href="https://fonts.googleapis.com/css2?family=Open+Sans:wght@400;600;700;800&display=swap" rel="stylesheet">
<style>
  :root {
    --backdrop: #8fa886;
    --card: #ffffff;
    --brand-green: #4f7a33;
    --paw-green: #a9c49c;
    --band-green: #b9cfae;
    --ink: #3a3a3a;
    --muted: #5c5c5c;
    --navy: #1f2e5a;
    --foliage: #8f9f80;
    --foliage-light: #b4c0a4;
    --coat: #a88566;
    --coat-dark: #6f5a48;
    --lawn: #c9c4ad;
    --veil: rgba(255, 255, 255, 0.32);
  }
  * { box-sizing: border-box; margin: 0; padding: 0; }
  html, body { width: 1200px; height: 914px; overflow: hidden; }
  body {
    background: var(--backdrop);
    font-family: "Open Sans", sans-serif;
    position: relative;
  }
  .card {
    position: absolute;
    top: 195px;
    width: 300px;
    height: 525px;
    background: var(--card);
    box-shadow: 0 10px 24px rgba(40, 60, 35, 0.25);
    overflow: hidden;
  }
  .card--front { left: 270px; }
  .card--back { left: 630px; }

  /* Front */
  .brand {
    position: absolute;
    top: 62px;
    left: 0;
    right: 0;
    display: flex;
    align-items: center;
    justify-content: center;
    gap: 8px;
    padding: 0 24px;
  }
  .brand__mark {
    width: 14px; height: 14px;
    background: var(--brand-green);
    flex: none;
  }
  .brand__name {
    color: var(--brand-green);
    font-weight: 700;
    font-size: 16px;
    line-height: 1.2;
    white-space: nowrap;
  }
  .person {
    position: absolute;
    top: 150px;
    left: 30px;
  }
  .person__name {
    color: var(--brand-green);
    font-size: 22px;
    font-weight: 400;
  }
  .person__name strong { font-weight: 800; }
  .person__title {
    color: var(--ink);
    font-size: 11px;
    letter-spacing: 0.5px;
    margin-top: 1px;
  }
  .contacts {
    position: absolute;
    top: 232px;
    left: 30px;
    list-style: none;
    color: var(--muted);
    font-size: 11.5px;
  }
  .contacts li {
    display: flex;
    align-items: flex-start;
    gap: 9px;
    margin-bottom: 9px;
    line-height: 1.45;
  }
  .contacts svg { flex: none; margin-top: 2px; }
  .paws {
    position: absolute;
    right: 26px;
    bottom: 48px;
    width: 80px;
    height: 120px;
    border-radius: 40px;
    background: linear-gradient(160deg, rgba(169,196,156,0.55), rgba(169,196,156,0.25));
  }

  /* Back */
  .photo {
    position: absolute;
    inset: 0;
    background:
      radial-gradient(ellipse 45% 38% at 48% 52%, var(--coat) 0%, rgba(168,133,102,0.6) 55%, rgba(168,133,102,0) 100%),
      radial-gradient(ellipse 40% 30% at 70% 80%, var(--coat-dark) 0%, rgba(111,90,72,0) 100%),
      radial-gradient(ellipse 55% 30% at 20% 12%, var(--foliage) 0%, rgba(143,159,128,0) 100%),
      linear-gradient(180deg, var(--foliage-light) 0%, var(--foliage) 30%, var(--lawn) 62%, #bfae98 100%);
  }
  .photo::after {
    content: "";
    position: absolute;
    inset: 0;
    background: var(--veil);
  }
  .back-paws {
    position: absolute;
    top: 24px;
    left: 28px;
    width: 80px;
    height: 80px;
    border-radius: 18px;
    background: rgba(169,196,156,0.75);
  }
  .back-brand {
    position: absolute;
    top: 40px;
    right: 18px;
    display: flex;
    align-items: center;
    gap: 6px;
    padding: 6px 8px;
    background: rgba(255,255,255,0.55);
  }
  .back-brand .brand__mark { width: 11px; height: 11px; background: var(--navy); }
  .back-brand .brand__name { color: var(--navy); font-size: 11.5px; }
  .web-band {
    position: absolute;
    left: 0; right: 0;
    bottom: 42px;
    height: 32px;
    background: var(--band-green);
    display: flex;
    align-items: center;
    justify-content: center;
    color: #ffffff;
    font-weight: 700;
    font-size: 13px;
  }
</style>
</head>
<body>
  <section class="card card--front">
    <div class="brand">
      <span class="brand__mark"></span>
      <span class="brand__name">Pine Ridge Canine Coaching</span>
    </div>
    <div class="person">
      <p class="person__name"><strong>Trevor</strong> Holloway</p>
      <p class="person__title">FOUNDER</p>
    </div>
    <ul class="contacts">
      <li>
        <svg width="12" height="12" viewBox="0 0 12 12"><circle cx="6" cy="6" r="6" fill="var(--brand-green)"/><path d="M6 2.5a2 2 0 0 0-2 2c0 1.5 2 4 2 4s2-2.5 2-4a2 2 0 0 0-2-2z" fill="#fff"/></svg>
        <span>000 North Ridge Rd., Suite 300,<br>Pine Hill, US 0000</span>
      </li>
      <li>
        <svg width="12" height="12" viewBox="0 0 12 12"><circle cx="6" cy="6" r="6" fill="var(--brand-green)"/><path d="M4 3h1.2l.6 1.6-.8.6a4 4 0 0 0 1.8 1.8l.6-.8 1.6.6V8a1 1 0 0 1-1 1A5 5 0 0 1 3 4a1 1 0 0 1 1-1z" fill="#fff"/></svg>
        <span>555-304-7162</span>
      </li>
      <li>
        <svg width="12" height="12" viewBox="0 0 12 12"><circle cx="6" cy="6" r="6" fill="var(--brand-green)"/><rect x="3" y="4" width="6" height="4" fill="#fff"/><path d="M3 4l3 2.2L9 4" stroke="var(--brand-green)" stroke-width="0.7" fill="none"/></svg>
        <span>info@pineridgecanine.example</span>
      </li>
      <li>
        <svg width="12" height="12" viewBox="0 0 12 12"><circle cx="6" cy="6" r="6" fill="var(--brand-green)"/><circle cx="6" cy="6" r="3" fill="none" stroke="#fff" stroke-width="0.8"/><path d="M3 6h6M6 3v6" stroke="#fff" stroke-width="0.7"/></svg>
        <span>www.pineridgecanine.example</span>
      </li>
    </ul>
    <div class="paws" role="img" aria-label="Trail of soft green paw prints"></div>
  </section>

  <section class="card card--back">
    <div class="photo" role="img" aria-label="Faded full-bleed photograph of a shepherd dog with a green collar in a leafy park"></div>
    <div class="back-paws" role="img" aria-label="Cluster of soft green paw prints"></div>
    <div class="back-brand">
      <span class="brand__mark"></span>
      <span class="brand__name">Pine Ridge Canine Coaching</span>
    </div>
    <div class="web-band">www.pineridgecanine.example</div>
  </section>
</body>
</html>
```